" O Instituto Raiz Clara tem como alicerce o fortalecimento e empoderamento do movimento que gere autonomia para a vida Consolidada há 20 anos num modelo de atuação multidisciplinar que desenvolve estratégias voltadas a promoção de uma vida sustentável e funcional. Nesse sentido consolidamos um trabalho junto a população menos favorecida e em vulnerabilidade social buscando estratégias de impacto nos eixos de atividade física, educação, cultura e lazer que capacitem o protagonismo de suas vidas. Para tanto atuamos com planejamento estratégico e ações práticas voltados a seguinte demanda: 1. Combate a Obesidade Infato Juvenil 2. Programa voltado a dependentes quimicos 3. Combate ao sedentarismo e obesidade 4. Programa voltado ao Envelhecimento Sustentável 5. Programa de inclusão através de atividades artisticas Entre outros "

```html
<!DOCTYPE html>
<html lang="pt-BR">
<head>
<meta charset="UTF-8">
<title>Instituto Raiz Clara — Fortalecer e Empoderar</title>
<link rel="stylesheet" href="https://fonts.googleapis.com/css2?family=Nunito:wght@600;700;800&display=swap">
<style>
  :root {
    --teal-deep: #1d6478;
    --teal-mid: #2f8ea3;
    --teal-light: #5fb7c4;
    --blush: #f8ecef;
    --white: #ffffff;
    --glow-gold: #f6c27a;
    --glow-rose: #e98fae;
    --glow-violet: #9a74b8;
  }
  * { margin: 0; padding: 0; box-sizing: border-box; }
  html, body { width: 1200px; height: 1200px; overflow: hidden; }
  body { font-family: "Nunito", sans-serif; background: var(--blush); }
  .poster { position: relative; width: 1200px; height: 1200px; overflow: hidden; background: var(--blush); }
  .poster__bands { position: absolute; inset: 0; }
  .hero-figure {
    position: absolute; left: 300px; top: 280px; width: 720px; height: 940px;
    border-radius: 50% 50% 0 0 / 40% 40% 0 0;
    background:
      radial-gradient(ellipse 45% 38% at 50% 62%, rgba(255,240,220,0.95), rgba(246,194,122,0.75) 40%, rgba(233,143,174,0.55) 70%, rgba(248,236,239,0) 100%),
      radial-gradient(ellipse 30% 40% at 50% 30%, rgba(233,143,174,0.5), rgba(154,116,184,0.25) 60%, rgba(248,236,239,0) 100%);
  }
  .headline {
    position: absolute; left: 46px; top: 26px; color: var(--white);
    line-height: 1.28;
  }
  .headline__lead { font-size: 44px; font-weight: 700; }
  .headline__main { font-size: 46px; font-weight: 800; }
  .brand {
    position: absolute; right: 36px; top: 90px; width: 300px;
    display: flex; flex-direction: column; align-items: center; gap: 14px;
    color: var(--teal-deep); font-weight: 800; text-align: center;
  }
  .brand__dot { width: 90px; height: 90px; border-radius: 50%; background: var(--teal-mid); }
  .brand__name { font-size: 34px; line-height: 1.1; letter-spacing: 1px; text-transform: uppercase; }
  .credit {
    position: absolute; left: 0; top: 970px; width: 730px; height: 150px;
    background: var(--teal-deep); color: var(--white);
    border-radius: 0 70px 70px 0; padding: 18px 0 0 34px;
  }
  .credit__name { font-size: 29px; font-weight: 800; line-height: 1.3; }
  .credit__role { font-size: 25px; font-weight: 600; line-height: 1.35; }
</style>
</head>
<body>
<main class="poster">
  <div class="hero-figure" role="img" aria-label="Silhueta luminosa de mulher com o braço erguido, com três pessoas caminhando sobre fundo em tons dourados, rosados e lilases"></div>

  <svg class="poster__bands" width="1200" height="1200" viewBox="0 0 1200 1200" aria-hidden="true">
    <path d="M0 0 H1200 V210 C1000 250 850 250 700 260 C450 275 200 300 0 330 Z" fill="var(--teal-light)"/>
    <path d="M0 0 H1200 V180 C1000 220 850 225 700 235 C450 250 200 270 0 300 Z" fill="var(--teal-deep)"/>
    <circle cx="1095" cy="150" r="300" fill="var(--white)"/>
    <circle cx="1095" cy="150" r="300" fill="none" stroke="var(--teal-light)" stroke-width="14"/>
    <path d="M760 1200 C880 1140 1040 1110 1200 1100 V1200 Z" fill="var(--teal-light)" opacity="0.7"/>
    <path d="M880 1200 C980 1160 1100 1145 1200 1140 V1200 Z" fill="var(--teal-deep)"/>
  </svg>

  <h1 class="headline">
    <span class="headline__lead">Fortalecer e Emponderar</span><br>
    <span class="headline__main">O MOVIMENTO que gere</span><br>
    <span class="headline__main">autonomia para a vida</span>
  </h1>

  <div class="brand">
    <span class="brand__dot"></span>
    <span class="brand__name">Instituto Raiz Clara</span>
  </div>

  <section class="credit">
    <p class="credit__name">Beatriz L. Moura</p>
    <p class="credit__role">Planejamento Estratégico de Projetos de Impacto Social</p>
    <p class="credit__role">Gestão de Programas em Promoção de Saúde</p>
  </section>
</main>
</body>
</html>
```